Book cover Design for her new book called 'Walking a path lined with courage and grace'

My name is Velorashi, I am the founder of The Quiet Lantern.
http://velorashi-wren.examplestore.com/
My book is an inspirational story of love and triumphing from adversity. After 40 years of surviving a life full of sexual abuse, physical and mental abuse and living with the effects of poor self-esteem and post traumatic stress disorder, this book is a guide to help others navigate away from negative emotions and help them find their own light in life. With the techniques developed and described in the book The Quiet Lantern's mission is to empower people with the journey to their own hearts and create warmth, love and inspiration.
The colours in the website represent the softness that I love and I prefer flowers. The colour also can be soft as well as vibrant and feminine. The final design should represent healing, love, inspiration and passion.

Target Market(s)

Women over the age of 25 -80
Teenagers suffering from depression
Men and women suffering from poor self esteem
Woman who have poor self confidence.

Requirements
Should not have
• Should not be dark in colour or imagery.

```html
<!DOCTYPE html>
<html lang="en">
<head>
<meta charset="utf-8">
<title>Walking a path lined with courage and grace — Velorashi</title>
<link rel="stylesheet" href="https://fonts.googleapis.com/css2?family=Righteous&family=Kalam:wght@300&family=Quicksand:wght@400&display=swap">
<style>
  :root {
    --sky-top: #1468ad;
    --sky-bottom: #1a7bc6;
    --sky-glow: rgba(120, 190, 240, 0.55);
    --field-top: #1a86d6;
    --field-bottom: #2396ea;
    --art-light: rgba(235, 245, 253, 0.9);
    --art-soft: rgba(200, 226, 246, 0.35);
    --ink-light: #ffffff;
    --ink-soft: #e8f3fc;
  }
  html, body {
    margin: 0;
    padding: 0;
    width: 768px;
    height: 1200px;
    overflow: hidden;
    background: var(--field-top);
  }
  .cover {
    position: relative;
    width: 768px;
    height: 1200px;
    overflow: hidden;
    background: linear-gradient(160deg, var(--field-top) 0%, var(--field-bottom) 100%);
  }
  .cover__sky {
    position: absolute;
    left: 0;
    top: 0;
    width: 768px;
    height: 590px;
    background:
      radial-gradient(ellipse 300px 230px at 600px 560px, var(--sky-glow) 0%, rgba(120,190,240,0) 100%),
      radial-gradient(ellipse 360px 300px at 0 590px, rgba(30,140,220,0.5) 0%, rgba(30,140,220,0) 100%),
      linear-gradient(180deg, var(--sky-top) 0%, var(--sky-bottom) 100%);
  }
  .cover__signpost {
    position: absolute;
    left: 450px;
    top: 262px;
    width: 240px;
    height: 328px;
    background:
      radial-gradient(ellipse 110px 46px at 120px 300px, var(--art-light) 0%, rgba(235,245,253,0.6) 60%, rgba(235,245,253,0) 100%),
      radial-gradient(ellipse 70px 170px at 124px 150px, var(--art-light) 0%, var(--art-soft) 65%, rgba(200,226,246,0) 100%);
  }
  .cover__title {
    position: absolute;
    right: 54px;
    top: 606px;
    margin: 0;
    font-family: "Righteous", "Trebuchet MS", sans-serif;
    font-weight: 400;
    font-size: 31px;
    line-height: 1;
    color: var(--ink-light);
    white-space: nowrap;
    text-transform: lowercase;
  }
  .cover__subtitle {
    position: absolute;
    right: 56px;
    top: 638px;
    margin: 0;
    font-family: "Kalam", "Comic Sans MS", cursive;
    font-weight: 300;
    font-style: italic;
    font-size: 21px;
    line-height: 1;
    letter-spacing: 2px;
    color: var(--ink-soft);
    white-space: nowrap;
  }
  .cover__author {
    position: absolute;
    right: 90px;
    bottom: 36px;
    margin: 0;
    font-family: "Quicksand", "Helvetica Neue", sans-serif;
    font-weight: 400;
    font-size: 34px;
    line-height: 1;
    color: var(--ink-light);
  }
</style>
</head>
<body>
  <main class="cover">
    <div class="cover__sky"></div>
    <div class="cover__signpost" role="img" aria-label="White silhouette of a crossroads signpost with pointing arrows on a small grassy mound"></div>
    <h1 class="cover__title">walking a path lined with courage and grace</h1>
    <p class="cover__subtitle">an inspirational story of love</p>
    <p class="cover__author">Velorashi</p>
  </main>
</body>
</html>
```